Business Cards for Orvanta LLC

We need business cards for a new company called “Orvanta LLC”. This is a technology process improvement company providing a comprehensive assessment of the technology used to run their business. The documentation and review process delivers the visibility and reassurance they need to protect their business and plan for the future. The product is called “Systems Mapwork”. Our primary target is small-medium size businesses, with the deliverables going to the decision maker. We would like to see the designs use the color blue. Our tag line is PROTECT YOUR BUSINESS · TAKE CONTROL OF IT.

Industry/Entity Type

Business

Contact Information for Business Card

Tag line should be on back of card - it does not have to be upper case.

Requirements
Must have
• Please use information when laying out card:
• Name: Gareth Pellham
• Title: Partner
• Phone Number: (844)555-0172
• Email: gareth@orvantallc-example.com
• Website: http://orvantallc-example.com

```html
<!DOCTYPE html>
<html lang="en">
<head>
<meta charset="utf-8">
<title>Business Cards for Orvanta LLC</title>
<link rel="stylesheet" href="https://fonts.googleapis.com/css2?family=Montserrat:wght@700&family=Questrial&display=swap">
<style>
  :root {
    --page-bg: #efefef;
    --brand-blue: #1673bf;
    --ink-blue: #0f5aa8;
    --ink-dark: #222222;
    --card-white: #fafafa;
    --white: #ffffff;
  }
  * { margin: 0; padding: 0; box-sizing: border-box; }
  html, body { width: 1200px; height: 586px; overflow: hidden; }
  body {
    background: var(--page-bg);
    font-family: "Questrial", sans-serif;
    position: relative;
  }
  .card {
    position: absolute;
    top: 129px;
    width: 502px;
    height: 301px;
  }
  .card--back { left: 61px; background: var(--brand-blue); color: var(--white); }
  .card--front { left: 619px; background: var(--card-white); }

  .back-name {
    position: absolute;
    left: 0; right: 0; top: 108px;
    text-align: center;
    font-family: "Questrial", sans-serif;
    font-size: 52px;
    letter-spacing: 3px;
    color: var(--white);
  }
  .tagline {
    position: absolute;
    left: 0; right: 0; top: 248px;
    text-align: center;
    font-size: 13.5px;
    letter-spacing: 0.3px;
  }

  .brand {
    position: absolute;
    left: 20px; width: 220px; top: 120px;
    display: flex; align-items: center; justify-content: center; gap: 8px;
    font-family: "Questrial", sans-serif;
    font-size: 25px;
    letter-spacing: 1px;
    color: var(--brand-blue);
  }
  .brand-mark { width: 14px; height: 14px; background: var(--brand-blue); }

  .divider {
    position: absolute;
    left: 257px; top: 71px;
    width: 2px; height: 168px;
    background: linear-gradient(to bottom, transparent, var(--brand-blue) 30%, var(--brand-blue) 70%, transparent);
  }
  .contact { position: absolute; left: 294px; top: 98px; }
  .contact-name {
    font-family: "Montserrat", sans-serif;
    font-size: 16px;
    color: var(--ink-blue);
    letter-spacing: 0.3px;
  }
  .contact-title { font-size: 10.5px; color: var(--ink-dark); margin-top: 6px; }
  .contact-line {
    display: flex; align-items: center; gap: 9px;
    font-size: 11.5px; color: var(--ink-dark);
    margin-top: 10px;
  }
  .contact-line:first-of-type { margin-top: 14px; }
  .icon { width: 16px; height: 16px; flex: none; }
  .contact-web {
    font-family: "Montserrat", sans-serif;
    font-size: 10.5px; color: var(--ink-blue);
    letter-spacing: 1.2px; margin-top: 9px;
  }
</style>
</head>
<body>
  <section class="card card--back" aria-label="Card back">
    <div class="back-name">Orvanta LLC</div>
    <p class="tagline">PROTECT YOUR BUSINESS &nbsp;·TAKE CONTROL OF IT.</p>
  </section>

  <section class="card card--front" aria-label="Card front">
    <div class="brand"><span class="brand-mark"></span>Orvanta LLC</div>
    <div class="divider"></div>
    <div class="contact">
      <h1 class="contact-name">GARETH PELLHAM</h1>
      <p class="contact-title">PARTNER</p>
      <p class="contact-line">
        <svg class="icon" viewBox="0 0 16 16" aria-hidden="true">
          <circle cx="8" cy="8" r="8" fill="var(--ink-blue)"/>
          <path d="M4.5 6.2c0-1 1.5-1.6 3.5-1.6s3.5.6 3.5 1.6v.6H10v-.5H6v.5H4.5z M5.5 7.5h5l.7 3.5H4.8z" fill="#fff"/>
        </svg>
        (844)555-0172
      </p>
      <p class="contact-line">
        <svg class="icon" viewBox="0 0 16 16" aria-hidden="true">
          <circle cx="8" cy="8" r="8" fill="var(--ink-blue)"/>
          <rect x="4" y="5" width="8" height="6" fill="#fff"/>
          <path d="M4 5l4 3.3L12 5" fill="none" stroke="var(--ink-blue)" stroke-width="0.9"/>
        </svg>
        gareth@orvantallc-example.com
      </p>
      <p class="contact-web">www.orvantallc-example.com</p>
    </div>
  </section>
</body>
</html>
```